Webdesign for recipe site

Please take a look at www.pfannenhaus.com. PH is a community site with around 60000 user recipes. It is a one-man-project and needs a redesign.
The new design shall meet these facts
high usability
1st focus on content
2nd focus on search and registration-elements
flat menü ? much content above the fold
well contured font type, size and color
coherent button, box and element design
useful design guide for the whole site
flexible font-sizes (changable css)
flexible color set for day and night mode (changable css)
And these facts shall not change
Keeping the „soul“ of pfannenhaus. PH is an independent and free recipe source. No media corporation. Everyone can participate.
This means, that PH is seen as a very personal, even private website and the design shall transport this. The design shall not be cold or heartless. It shall work and leave a cheerful impression as well. The design shall keep the atmosphere of a one-man-project, where everyone is welcomed and the personal touch is warm and heartly.
Since 8 years, the major color is red. The tone must be kept while the intensitity shall be lowered. A decent background and a warm and welltought color set are wanted in a way, that the tone of the website is still seen as red. Probably the links shall remain red, that way the rest can be set less intense.
And these facts are open
The design elements are the cook and the red tomato. While it would be nice to keep the cook (not required at any means), the tomato could be dropped. If they fit into a new design – great, if not, it's ok.
Example Pages
Recipe: http://www.pfannenhaus.com/r/68765-panini-vereinfachte-variation.html
Category: http://www.pfannenhaus.com/kb/0k0/Backrezept/rezepte.html
Homepage: http://www.pfannenhaus.com
Updates
A nice color set: http://www.artquorra.com/design/463831
A well structured design: http://www.artquorra.com/design/452858
Reason: Just 3 days left and no submission yet.
We will guarantee the project payment (thanks for hinting, Tavin) and extend the deadline by 7 days.
Thank you for your submissions.
The brown/red/beige color-sets are good, they lead the way. The layout though is mostly too playful. It shall be clean and simple and likely to fit for all the content, for the single recipe as well as the recipe lists, the profile page and the homepage.
I got inspired by you color sets and set up a testpage that pretty much goes in to the direction I want. Very flat header, peaceful and warm colors, no distraction, focus on the content. What's still missing is the breadcrumb section and an idea to fill the homepage and the recipe lists. And probably the colors (especially the light background-color, is it beige?) can also be better choosen.
Please see http://www.pfannenhaus.com/test-543677423/r_v01.html
Kind regards, Lukas
Reason: I extend the deadline once more to give Volbrin Designs the opportunity to participate. It would be nice to see drafts that go more into the clean and simple direction as I updated in the brief. Here is the current status: http://www.pfannenhaus.com/r/60262-steak-auf-spargel.html (is on test now). Maybe the beige-colors can be choosen more cleaner and suggestions for the homepage and recipe lists and the footer are very welcome also. Looking forward for your designs!
I'll put the Feedback on the latest design of quietmaple in the brief, so you all find it.
http://www.artquorra.com/design/587249/web-design-by-quietmaple
-
Dont't know man, this still doesn't look as clean as I need it. There are 100s of recipe sites online and it is urgent to design the page with clear focus on the content. As little distraction as possible, there will be ads for that.
Mainly, you did too much. There are too many design elements and the round bites with the squares. The header shall be as small as in the mentioned page: http://www.pfannenhaus.com/r/60262-steak-auf-spargel.html
I show you an example of a clean page as I see it: http://www.webtalvo.org/q/ips-and-domains
These are not the colors I want but they all fit together. I also need the font larger and the basic color scheme must be warmer. But maybe you can understand where I'm going or where I want to go.
Please do it very simple, with no corners, as flat and clean as possible, with a genuine feeling on first site of where the content is, what the focus of the site is (content).
Thank's.
Target Market(s)
age 35-55, majority is female, interested in recipes, cooking, baking
Industry/Entity Type
Media
Look and feel

```html
<!DOCTYPE html>
<html lang="de">
<head>
<meta charset="utf-8">
<title>Pfannenhaus – Start</title>
<link href="https://fonts.googleapis.com/css2?family=Source+Sans+3:ital,wght@0,400;0,600;0,700;1,700&display=swap" rel="stylesheet">
<style>
:root{
  --brand-red:#b71c24;
  --link-red:#c0272d;
  --button-red:#e8462a;
  --ink:#111111;
  --panel-dark:#333333;
  --paper:#ffffff;
  --photo-a:#a9aeb0;
  --photo-b:#7fa55a;
}
*{box-sizing:border-box;margin:0;padding:0}
html,body{width:1041px;height:1200px;overflow:hidden;background:var(--paper)}
body{position:relative;font-family:"Source Sans 3",Arial,sans-serif;color:var(--ink)}
.abs{position:absolute}

/* header */
.brand{left:32px;top:112px;font-size:56px;font-weight:700;color:var(--brand-red);letter-spacing:-0.5px;line-height:1}
.login-shape{left:651px;top:0;width:390px;height:236px}
.login-label{color:#fff;font-size:25px;text-align:right;width:110px;left:658px;line-height:1}
.login-input{left:776px;width:225px;height:34px;background:#fff;border:none}
.login-button{left:801px;top:114px;width:224px;height:48px;background:var(--button-red);color:#fff;
  border-radius:8px;font-size:24px;display:flex;align-items:center;justify-content:center;white-space:nowrap}

/* navigation */
.red-band{left:0;top:307px;width:1028px;height:772px;background:var(--brand-red)}
.start-tab{left:0;top:221px;width:247px;height:90px;background:var(--brand-red);border-radius:0 10px 0 0;
  color:#fff;font-size:56px;display:flex;align-items:center;justify-content:center;padding-bottom:4px}
.nav{left:247px;top:245px;width:781px;height:62px;display:flex}
.nav-item{background:#fff;border:1px solid #999;border-bottom:none;color:var(--link-red);font-size:23px;
  display:flex;align-items:center;justify-content:center;height:62px}
.nav-item:last-child{border-radius:0 8px 0 0}

/* content panel */
.content{left:26px;top:338px;width:974px;height:709px;background:#fff;border-radius:18px;border:1px solid #555}
.intro-title{left:42px;top:362px;font-size:26px;color:var(--link-red);font-weight:400}
.intro-text{left:42px;top:423px;font-size:17px;line-height:22px}

.section-label{left:34px;height:40px;background:var(--brand-red);color:#fff;font-size:19px;
  display:flex;align-items:center;padding-left:10px}
.section-arrows{height:40px}
.list{list-style:none;left:32px}
.list li{display:flex;align-items:baseline;white-space:nowrap;line-height:1}
.num{color:var(--link-red);font-weight:700;font-size:21px;width:24px}
.item-text{font-size:14px}
.lead .num{font-size:34px;width:30px}
.lead .item-text{font-size:23px}
.more-link{left:39px;font-size:22px;font-weight:700;color:var(--link-red)}

/* feature box */
.feature{left:591px;top:361px;width:381px;height:530px;border:1px solid #777}
.feature-photo{left:591px;top:361px;width:381px;height:284px;
  background:linear-gradient(160deg,var(--photo-a) 0%,#b9c2b0 45%,var(--photo-b) 100%)}
.feature-bar{left:591px;top:645px;width:381px;height:40px;background:var(--brand-red);color:#fff;font-size:19px;
  display:flex;align-items:center;justify-content:center}
.bar-arrow{position:absolute;top:10px}
.feature-list{left:600px;top:697px;list-style:none;font-size:14px;line-height:19.2px}
.feature-more{left:600px;top:802px;width:362px;text-align:center;font-size:15px;font-weight:700;font-style:italic;
  color:var(--link-red);line-height:19px}

/* footer */
.footer{left:0;top:1079px;width:1028px;height:120px;background:#fff;border:1px solid #777;border-top:none;border-radius:0 0 10px 0}
.footer-col{top:1090px;text-align:center;font-size:14px;font-weight:700;color:var(--link-red);line-height:17px}
</style>
</head>
<body>

<div class="abs brand">Pfannenhaus</div>

<svg class="abs login-shape" viewBox="0 0 390 236" aria-hidden="true">
  <path d="M0 0 H390 V150 Q390 192 370 192 L350 192 Q352 220 368 236 Q320 228 305 192 L30 192 Q0 192 0 162 Z" fill="var(--panel-dark)"/>
</svg>
<div class="abs login-label" style="top:22px">Login:</div>
<div class="abs login-label" style="top:60px">Passwort:</div>
<div class="abs login-input" style="top:15px"></div>
<div class="abs login-input" style="top:55px"></div>
<div class="abs login-button">Login Pfannenhaus</div>

<div class="abs red-band"></div>
<div class="abs start-tab">Start</div>
<nav class="abs nav">
  <div class="nav-item" style="width:160px">Rezepte</div>
  <div class="nav-item" style="width:157px">Magazin</div>
  <div class="nav-item" style="width:153px">Foren</div>
  <div class="nav-item" style="width:153px">Gemeinschaft</div>
  <div class="nav-item" style="width:158px">Markt</div>
</nav>

<div class="abs content"></div>

<h1 class="abs intro-title">Rezepte tauschen? Pfannenhaus!</h1>
<p class="abs intro-text">Du liebst gute Rezepte? Willkommen bei Pfannenhaus.<br>
Hier findest du tausende Rezepte, viele mit Bild.<br>
Du kannst jedes Rezept speichern und kommentieren.<br>
Und du kannst sofort deine eigenen<br>
Rezepte und Bilder hochladen.<br>
Ohne Wartezeiten. Los geht's.</p>

<div class="abs section-label" style="top:565px;width:149px">Neue Rezepte</div>
<svg class="abs section-arrows" style="left:185px;top:565px;width:42px" viewBox="0 0 42 40" aria-hidden="true">
  <path d="M0 0 L20 20 L0 40 Z M21 0 L41 20 L21 40 Z" fill="var(--brand-red)"/>
</svg>
<ol class="abs list" style="top:613px">
  <li class="lead" style="height:44px"><span class="num">1.</span><span class="item-text">Schweinebauch mit Semmelfülle</span></li>
  <li style="height:25px"><span class="num">2.</span><span class="item-text">Rote Bete mit Chinakohl und In...</span></li>
  <li style="height:24px"><span class="num">3.</span><span class="item-text">Hanna's Fichtenspitzenessig</span></li>
  <li style="height:26px"><span class="num">4.</span><span class="item-text">Ungarischer Krautsalat</span></li>
  <li style="height:24px"><span class="num">5.</span><span class="item-text">Spagetti mit Champignoncarbona...</span></li>
</ol>
<div class="abs more-link" style="top:747px">weitere neue Rezepte</div>

<div class="abs section-label" style="top:805px;width:199px">Aktuell in den Foren</div>
<svg class="abs section-arrows" style="left:236px;top:805px;width:54px" viewBox="0 0 54 40" aria-hidden="true">
  <path d="M0 0 L24 20 L0 40 Z M27 0 L51 20 L27 40 Z" fill="var(--brand-red)"/>
</svg>
<ol class="abs list" style="top:853px">
  <li style="height:23px"><span class="num">1.</span><span class="item-text">Neues Spiel: Ahnungen</span></li>
  <li style="height:23px"><span class="num">2.</span><span class="item-text">ein kleines Spiel...</span></li>
  <li style="height:23px"><span class="num">3.</span><span class="item-text">Krankenhaus</span></li>
  <li style="height:25px"><span class="num">4.</span><span class="item-text">Sabine1 feiert heute....</span></li>
  <li style="height:23px"><span class="num">5.</span><span class="item-text">5. Melde mich für eine Zeit mal ab ...</span></li>
</ol>
<div class="abs more-link" style="top:971px">weitere aktuelle Forenbeiträge</div>

<div class="abs feature"></div>
<div class="abs feature-photo" role="img" aria-label="Foto: Feldsalat mit Champignons auf einem Glasteller"></div>
<div class="abs feature-bar">
  <svg class="bar-arrow" style="left:10px" width="16" height="22" viewBox="0 0 16 22" aria-hidden="true"><path d="M16 0 L0 11 L16 22 Z" fill="#fff"/></svg>
  Feldsalat &amp; Grünkohl
  <svg class="bar-arrow" style="right:10px" width="16" height="22" viewBox="0 0 16 22" aria-hidden="true"><path d="M0 0 L16 11 L0 22 Z" fill="#fff"/></svg>
</div>
<ul class="abs feature-list">
  <li>- Marens Feldsalat mit Champis</li>
  <li>- Grünkohl mit Pinkel und Hamburger süßen Kartoffeln</li>
  <li>- Gebratener Rosenkohl</li>
  <li>- Vogerlsalat mit Himbeeren und Speck</li>
  <li>- Chicoree im Strudelteig</li>
</ul>
<p class="abs feature-more">und außerdem alle Rezepte für Feldsalat (202),<br>Grünkohl (102), Rosenkohl (188), Chicoree (164),<br>und Pastinaken (54)</p>

<footer>
  <div class="abs footer"></div>
  <div class="abs footer-col" style="left:171px;width:200px">Newsletter<br>RSS: Rezept des Tages<br>RSS: Neue Rezepte</div>
  <div class="abs footer-col" style="left:402px;width:200px">Impressum | Kontakt<br>Team | Urheberrecht<br>AGB | Regeln<br>Hier werben | Stats<br>Externe Nutzung</div>
  <div class="abs footer-col" style="left:641px;width:200px">Surftipps:<br>Cocktails<br>Sportecke<br>Espressomaschine<br>www.kuechenglueck.at<br>Herdwerk</div>
</footer>

</body>
</html>
```